Real Estate For Sale Signage

I'm an independent agent in Lismore NSW Australia with high standards and looking for a catching 'For Sale'sign board.
I like classy, elegant, stylish and simple best.
My colours are red, white and black.
I don't have a logo or other font designs I need to stick to. I like the concept of a house or real estate design.
Before I created this project I played around on publisher and created the PDF attached. I'm not sold on it, but I don't mind the way the name has been layed out. Originally I had a white background with black & red font.
Fancy fonts for my name would be nice, but must not be busy.
Updates

Just wanted to advise that I have updated my brief and used the tools available to help get my ideas through.

Thank you for your work and time.

Kind regards
Marella

Industry/Entity Type

Real Estate

Requirements
Must have
• For Sale
Marella Quint Real Estate (must stand out)
0400 517 382 (must stand out)
17 Tallowood Street North Lismore
www.marellaquintrealestate.com.au

```html
<!DOCTYPE html>
<html lang="en">
<head>
<meta charset="utf-8">
<title>For Sale – Marella Quint Real Estate</title>
<link rel="stylesheet" href="https://fonts.googleapis.com/css2?family=Fredoka:wght@700&family=Marcellus&family=Playfair+Display:ital,wght@1,800&family=Tinos&display=swap">
<style>
  :root {
    --sign-red: #c7383a;
    --sign-red-deep: #b3292c;
    --sign-white: #ffffff;
    --sign-black: #111111;
  }
  html, body {
    margin: 0;
    padding: 0;
    overflow: hidden;
    background: var(--sign-white);
  }
  .sign {
    position: relative;
    width: 900px;
    height: 1200px;
    background: var(--sign-red);
    overflow: hidden;
    color: var(--sign-white);
  }
  .sign__decoration {
    position: absolute;
    inset: 0;
    width: 900px;
    height: 1200px;
  }
  .sign__headline {
    position: absolute;
    top: 148px;
    left: 0;
    width: 840px;
    margin: 0;
    text-align: center;
    font-family: "Fredoka", sans-serif;
    font-weight: 700;
    font-size: 150px;
    line-height: 1;
    letter-spacing: 2px;
    white-space: nowrap;
  }
  .sign__with {
    position: absolute;
    top: 318px;
    left: 0;
    width: 842px;
    text-align: center;
    font-family: "Playfair Display", serif;
    font-style: italic;
    font-weight: 800;
    font-size: 40px;
    line-height: 1;
  }
  .sign__agent {
    position: absolute;
    top: 372px;
    left: 0;
    width: 900px;
    text-align: center;
    font-family: "Marcellus", serif;
    font-size: 124px;
    line-height: 1;
    white-space: nowrap;
    letter-spacing: -1px;
  }
  .sign__agent-initial {
    font-size: 164px;
  }
  .sign__agency {
    position: absolute;
    top: 568px;
    right: 24px;
    font-family: "Marcellus", serif;
    font-size: 118px;
    line-height: 1;
    white-space: nowrap;
  }
  .sign__phone-label {
    position: absolute;
    top: 906px;
    left: 24px;
    font-family: "Playfair Display", serif;
    font-style: italic;
    font-weight: 800;
    font-size: 40px;
    line-height: 1;
  }
  .sign__phone {
    position: absolute;
    top: 956px;
    left: 0;
    width: 900px;
    text-align: center;
    font-family: "Fredoka", sans-serif;
    font-weight: 700;
    font-size: 116px;
    line-height: 1;
    letter-spacing: 8px;
    white-space: nowrap;
  }
  .sign__footer {
    position: absolute;
    left: 0;
    bottom: 0;
    width: 900px;
    height: 124px;
    background: var(--sign-white);
    color: var(--sign-black);
    font-family: "Tinos", serif;
    text-align: center;
  }
  .sign__address {
    margin: 8px 0 0;
    font-size: 46px;
    line-height: 1.1;
    letter-spacing: 5.5px;
    white-space: nowrap;
  }
  .sign__website {
    margin: 4px 0 0;
    font-size: 38px;
    line-height: 1.1;
    letter-spacing: 9px;
    white-space: nowrap;
  }
</style>
</head>
<body>
  <main class="sign">
    <svg class="sign__decoration" viewBox="0 0 900 1200" role="img" aria-label="Decorative diagonal band of red roof tiles">
      <defs>
        <linearGradient id="tileBand" x1="0" y1="0" x2="1" y2="1">
          <stop offset="0" stop-color="var(--sign-red-deep)"/>
          <stop offset="1" stop-color="var(--sign-red)"/>
        </linearGradient>
      </defs>
      <polygon points="660,0 900,0 900,880 660,640 400,220" fill="url(#tileBand)"/>
    </svg>

    <h1 class="sign__headline">For Sale</h1>
    <div class="sign__with">With</div>

    <div class="sign__agent"><span class="sign__agent-initial">M</span>arella <span class="sign__agent-initial">Q</span>uint</div>
    <div class="sign__agency">Real Estate</div>

    <div class="sign__phone-label">Telephone:</div>
    <div class="sign__phone">0400 517 382</div>

    <footer class="sign__footer">
      <p class="sign__address">17 Tallowood Street North Lismore</p>
      <p class="sign__website">www.marellaquintrealestate.com.au</p>
    </footer>
  </main>
</body>
</html>
```